Van wrap design for 2014 Marlow T310 Commercial Van

We are launching a maintenance division for our property company and have bought a new van to advertise our maintenance company. We will be advertising to property owners, the general public etc. our services.
We wish the text to read: Maintenance Division - remodels, plumbing & electrical.

Requirements
Must have
• Both images attached

```html
<!DOCTYPE html>
<html lang="en">
<head>
<meta charset="utf-8">
<title>Harland Peak Properties – Maintenance Division Van Wrap</title>
<link rel="stylesheet" href="https://fonts.googleapis.com/css2?family=Archivo:wght@800;900&family=Roboto:wght@400;700&display=swap">
<style>
  :root {
    --stage: #6d777d;
    --wrap-white: #f4f7fa;
    --wrap-ice: #cfe2f2;
    --wrap-sky: #8fc0e6;
    --wrap-blue: #3f8fd0;
    --band-green: #4fd97a;
    --band-green-deep: #36c463;
    --frame-blue: #2f45c4;
    --ink-white: #ffffff;
    --phone-outline: #2f7fd1;
  }
  * { box-sizing: border-box; margin: 0; padding: 0; }
  html, body { width: 1200px; height: 862px; overflow: hidden; }
  body { background: var(--stage); position: relative; font-family: "Roboto", Arial, sans-serif; }

  .wrap-side {
    position: absolute; left: 50px; top: 180px; width: 1100px; height: 500px;
    border-radius: 18px; overflow: hidden;
  }
  .wrap-art { position: absolute; inset: 0; width: 100%; height: 100%; }

  .headline {
    position: absolute; left: 500px; top: 50px;
    transform: rotate(9deg); transform-origin: left top;
    color: var(--ink-white);
    font-family: "Archivo", "Arial Black", sans-serif;
  }
  .headline__title { font-size: 40px; font-weight: 900; letter-spacing: -0.5px; line-height: 1; white-space: nowrap; }
  .headline__services {
    font-size: 16px; font-weight: 800; line-height: 1.2; margin: 4px 0 0 48px; white-space: nowrap;
  }
  .headline__phone {
    font-size: 34px; font-weight: 900; line-height: 1; margin: 38px 0 0 40px; white-space: nowrap;
    color: var(--ink-white);
    -webkit-text-stroke: 2px var(--phone-outline);
    paint-order: stroke fill;
    text-shadow: 0 0 6px rgba(255,255,255,0.9);
  }

  .team-photo {
    position: absolute; left: 230px; top: 225px; width: 170px; height: 165px;
    border: 4px solid var(--frame-blue);
    background: linear-gradient(160deg, #7fa7c4 0%, #3c5874 55%, #2a3a52 100%);
  }

  .contact-lines {
    position: absolute; left: 236px; top: 402px;
    transform: rotate(-3deg); transform-origin: left top;
    color: var(--ink-white); font-size: 13px; line-height: 1.3;
  }
</style>
</head>
<body>
  <section class="wrap-side" aria-label="Van side wrap">
    <svg class="wrap-art" viewBox="0 0 1100 500" aria-hidden="true">
      <defs>
        <linearGradient id="wrapBase" x1="0" y1="0" x2="1" y2="0.3">
          <stop offset="0" stop-color="var(--wrap-white)"/>
          <stop offset="0.35" stop-color="var(--wrap-ice)"/>
          <stop offset="0.7" stop-color="var(--wrap-sky)"/>
          <stop offset="1" stop-color="var(--wrap-blue)"/>
        </linearGradient>
        <linearGradient id="greenBand" x1="0" y1="0" x2="1" y2="0">
          <stop offset="0" stop-color="var(--band-green-deep)"/>
          <stop offset="1" stop-color="var(--band-green)"/>
        </linearGradient>
      </defs>
      <rect class="wrap-base" width="1100" height="500" fill="url(#wrapBase)"/>
      <g class="speed-streaks" fill="#ffffff" opacity="0.35">
        <polygon points="300,120 1100,210 1100,225 300,140"/>
        <polygon points="420,300 1100,360 1100,372 420,316"/>
        <polygon points="200,440 1100,470 1100,480 200,456"/>
        <polygon points="600,20 1100,60 1100,68 600,30"/>
      </g>
      <g class="facets" fill="var(--wrap-blue)" opacity="0.25">
        <polygon points="520,300 700,340 640,440 480,410"/>
        <polygon points="760,340 980,370 920,470 720,450"/>
        <polygon points="850,20 1060,40 1000,70 820,60"/>
      </g>
      <polygon class="green-band" points="430,0 620,0 1100,76 1100,235 520,143" fill="url(#greenBand)" opacity="0.95"/>
      <polygon class="green-band-tail" points="440,0 500,0 560,60 480,50" fill="var(--band-green)" opacity="0.7"/>
    </svg>

    <div class="headline">
      <h1 class="headline__title">MAINTENANCE DIVISION</h1>
      <p class="headline__services">REMODELS, PLUMBING &amp; ELECTRICAL</p>
      <p class="headline__phone">+1 555-014-2297</p>
    </div>

    <div class="team-photo" role="img" aria-label="Photo of the two company owners in suits"></div>

    <div class="contact-lines">
      <p>+1 555-014-2297</p>
      <p>www.harlandpeakproperties.com</p>
      <p>www.harlandpeak.social/HarlandPeakProperties</p>
    </div>
  </section>
</body>
</html>
```